User Interface Designer Needed

I need a few designs for a property law comparison website. We assist the public with finding a solicitor for the purchase or sale of their house and units. We are currently in the process of creating a questionnaire based woo commerce product filter using gravity forms. I'd like to see designs that use the logo colours. Users will be selecting options such as "Buying" or "Selling", they will then be selecting options such as "House" "Unit" or "Land". Details attached. The final design should communicate ease and simplicity. Questions will be answered one at a time, and the next question is dependent on the answer to the question prior

Target Market(s)

First home buyers, people from ages 18-80 make and female looking to get rid of the hassle of ringing around and going from website to website trying to get a quote

Industry/Entity Type

Real Estate

Number of Pages Required

1 page

Colors
33a6d7

Requirements
Must have
• A design for every question
Nice to have
• Simple symbols or simplistic pictures incorporated, even better if you can turn the question into a picture instead of words eg. A picture of a house, a picture of a unit and a picture of land instead of written answers

```html
<!DOCTYPE html>
<html lang="en">
<head>
<meta charset="utf-8">
<title>Property Solicitor Quote Questionnaire</title>
<link rel="stylesheet" href="https://fonts.googleapis.com/css2?family=Oswald:wght@600;700&family=Ubuntu:wght@400&display=swap">
<style>
  :root {
    --brand: #33a6d7;
    --ink: #333333;
    --bg: #eeeeef;
    --card: #ffffff;
    --box-line: #cfcfcf;
    --tick: #1a9b4b;
    --help: #f7941d;
    --frame: #6b6b6b;
    --figure: #d9e9f2;
  }
  * { box-sizing: border-box; margin: 0; padding: 0; }
  html, body { width: 1200px; height: 1200px; overflow: hidden; }
  body { background: var(--bg); position: relative; font-family: "Oswald", sans-serif; }

  .character {
    position: absolute;
    border-radius: 48% 48% 40% 40%;
    background: linear-gradient(180deg, #ffffff 0%, var(--figure) 45%, var(--brand) 100%);
    opacity: .55;
  }

  .card {
    position: absolute;
    background: var(--card);
    border: 1px solid #e0e0e0;
    box-shadow: 0 2px 6px rgba(0,0,0,.18);
  }
  .card-title {
    position: absolute; left: 10px; top: 4px;
    font-size: 32px; font-weight: 700; color: var(--ink);
    letter-spacing: -.5px; transform: scaleX(.86); transform-origin: left;
    white-space: nowrap;
  }
  .option {
    position: absolute; display: flex; align-items: center;
    transform: translateY(-50%);
  }
  .option-label {
    font-size: 23px; font-weight: 700; color: var(--brand);
    line-height: 1.15; white-space: nowrap;
    transform: scaleX(.86); transform-origin: left;
  }
  .icon { position: absolute; transform: translateY(-50%); fill: var(--brand); }
  .checkbox {
    position: absolute; width: 38px; height: 38px;
    border: 2px solid var(--box-line); border-radius: 8px;
    transform: translateY(-50%); background: #fff;
  }
  .checkbox svg { position: absolute; left: 2px; top: -10px; }
  .help {
    display: inline-block; width: 17px; height: 17px; margin-left: 6px;
    border: 1.5px solid var(--help); border-radius: 50%;
    color: var(--help); font: 400 12px/14px "Ubuntu", sans-serif; text-align: center;
    vertical-align: middle;
  }

  .tooltip {
    position: absolute; left: 640px; top: 478px; width: 252px; height: 252px;
    background: var(--frame); padding: 12px;
  }
  .tooltip-body { background: #fff; width: 100%; height: 100%; padding: 10px 8px; font-family: "Ubuntu", sans-serif; color: var(--ink); }
  .tooltip-title { font-size: 17px; margin-bottom: 12px; }
  .tooltip-list { list-style: none; }
  .tooltip-list li { position: relative; padding-left: 26px; font-size: 15.5px; line-height: 1.35; margin-bottom: 9px; }
  .tooltip-list li::before {
    content: ""; position: absolute; left: 2px; top: 5px; width: 8px; height: 8px;
    border: 1.5px solid var(--brand); border-radius: 50%;
  }
</style>
</head>
<body>

<svg width="0" height="0" style="position:absolute">
  <defs>
    <symbol id="tick" viewBox="0 0 48 40"><path d="M4 20 L18 34 L44 4" fill="none" stroke="#1a9b4b" stroke-width="7" stroke-linecap="round" stroke-linejoin="round"/></symbol>
    <symbol id="house" viewBox="0 0 56 44"><path d="M2 22 L28 4 L54 22 L50 22 L50 42 L6 42 L6 22 Z"/><rect x="12" y="26" width="8" height="7" fill="#fff"/><rect x="24" y="26" width="8" height="16" fill="#fff"/><rect x="36" y="26" width="8" height="7" fill="#fff"/></symbol>
    <symbol id="land" viewBox="0 0 56 52"><path d="M28 2 L40 18 L34 18 L46 32 L38 32 L52 46 L4 46 L18 32 L10 32 L22 18 L16 18 Z"/><rect x="25" y="44" width="6" height="8"/><rect x="2" y="48" width="52" height="3"/></symbol>
    <symbol id="unit" viewBox="0 0 52 48"><rect x="2" y="4" width="48" height="44"/><g fill="#fff"><rect x="8" y="10" width="7" height="6"/><rect x="22" y="10" width="7" height="6"/><rect x="36" y="10" width="7" height="6"/><rect x="8" y="21" width="7" height="6"/><rect x="22" y="21" width="7" height="6"/><rect x="36" y="21" width="7" height="6"/><rect x="8" y="32" width="7" height="6"/><rect x="36" y="32" width="7" height="6"/><rect x="22" y="34" width="7" height="14"/></g></symbol>
    <symbol id="houseland" viewBox="0 0 56 52"><path d="M18 2 L28 16 L24 16 L32 28 L4 28 L12 16 L8 16 Z"/><path d="M20 32 L38 20 L56 32 L52 32 L52 50 L24 50 L24 32 Z"/><rect x="2" y="48" width="52" height="3"/><rect x="35" y="38" width="6" height="12" fill="#fff"/></symbol>
  </defs>
</svg>

<div class="character" style="left:248px;top:32px;width:120px;height:208px" role="img" aria-label="Cartoon character standing beside the first question"></div>
<div class="character" style="left:60px;top:368px;width:136px;height:208px" role="img" aria-label="Cartoon character holding the buying card"></div>
<div class="character" style="left:1020px;top:360px;width:108px;height:216px" role="img" aria-label="Cartoon character holding the selling card"></div>
<div class="character" style="left:60px;top:824px;width:140px;height:208px" role="img" aria-label="Cartoon character holding the quote card"></div>
<div class="character" style="left:1000px;top:832px;width:140px;height:212px" role="img" aria-label="Cartoon character holding the contract card"></div>
<div class="character" style="left:276px;top:960px;width:112px;height:208px" role="img" aria-label="Cartoon character pointing at the last question"></div>

<!-- Role -->
<section class="card" style="left:392px;top:28px;width:416px;height:216px">
  <h2 class="card-title">I AM A ?</h2>
  <svg class="icon" style="left:10px;top:78px" width="46" height="44" viewBox="0 0 46 44"><path d="M15 4 L31 4 L27 12 C40 18 44 28 42 36 C40 42 34 43 23 43 C12 43 6 42 4 36 C2 28 6 18 19 12 Z"/><text x="23" y="35" font-family="Ubuntu,sans-serif" font-size="18" fill="#fff" text-anchor="middle">$</text></svg>
  <div class="option" style="left:66px;top:78px"><span class="option-label">BUYER</span></div>
  <div class="checkbox" style="left:364px;top:78px"><svg width="48" height="40"><use href="#tick"/></svg></div>

  <svg class="icon" style="left:8px;top:130px" width="50" height="46" viewBox="0 0 50 46"><path d="M30 2 L48 2 L48 18 L20 44 L4 28 Z"/><circle cx="40" cy="10" r="3" fill="#fff"/><text x="25" y="30" font-family="Ubuntu,sans-serif" font-size="16" fill="#fff" text-anchor="middle" transform="rotate(-45 25 26)">$</text></svg>
  <div class="option" style="left:66px;top:128px"><span class="option-label">SELLER</span></div>
  <div class="checkbox" style="left:364px;top:128px"></div>

  <svg class="icon" style="left:8px;top:182px" width="52" height="48" viewBox="0 0 52 48"><g fill="none" stroke="#33a6d7" stroke-width="4"><path d="M12 4 L12 40 M4 32 L12 42 L20 32"/><path d="M40 44 L40 8 M32 16 L40 6 L48 16"/><rect x="18" y="12" width="16" height="24" rx="3"/></g><text x="26" y="30" font-family="Ubuntu,sans-serif" font-size="14" fill="#33a6d7" text-anchor="middle">$</text></svg>
  <div class="option" style="left:66px;top:182px"><span class="option-label">BUYER &amp; SELLER</span></div>
  <div class="checkbox" style="left:364px;top:182px"></div>
</section>

<!-- Buying -->
<section class="card" style="left:178px;top:260px;width:414px;height:216px">
  <h2 class="card-title">I AM BUYING A ?</h2>
  <svg class="icon" style="left:10px;top:90px" width="56" height="44"><use href="#house"/></svg>
  <div class="option" style="left:76px;top:90px"><span class="option-label">HOUSE</span></div>
  <div class="checkbox" style="left:160px;top:90px"></div>
  <svg class="icon" style="left:222px;top:88px" width="54" height="52"><use href="#land"/></svg>
  <div class="option" style="left:288px;top:90px"><span class="option-label">LAND</span></div>
  <div class="checkbox" style="left:368px;top:90px"></div>

  <svg class="icon" style="left:10px;top:172px" width="52" height="48"><use href="#unit"/></svg>
  <div class="option" style="left:76px;top:172px"><span class="option-label">UNIT</span></div>
  <div class="checkbox" style="left:160px;top:172px"><svg width="48" height="40"><use href="#tick"/></svg></div>
  <svg class="icon" style="left:222px;top:170px" width="54" height="52"><use href="#houseland"/></svg>
  <div class="option" style="left:288px;top:172px"><span class="option-label">HOUSE<br>&amp;LAND</span></div>
  <div class="checkbox" style="left:368px;top:172px"></div>
</section>

<!-- Selling -->
<section class="card" style="left:608px;top:260px;width:416px;height:216px">
  <h2 class="card-title">I AM SELLING A ?</h2>
  <svg class="icon" style="left:10px;top:90px" width="56" height="44"><use href="#house"/></svg>
  <div class="option" style="left:76px;top:90px"><span class="option-label">HOUSE</span></div>
  <div class="checkbox" style="left:160px;top:90px"></div>
  <svg class="icon" style="left:222px;top:88px" width="54" height="52"><use href="#land"/></svg>
  <div class="option" style="left:288px;top:90px"><span class="option-label">LAND</span></div>
  <div class="checkbox" style="left:368px;top:90px"></div>

  <svg class="icon" style="left:10px;top:172px" width="52" height="48"><use href="#unit"/></svg>
  <div class="option" style="left:76px;top:172px"><span class="option-label">UNIT</span></div>
  <div class="checkbox" style="left:160px;top:172px"></div>
  <svg class="icon" style="left:222px;top:170px" width="54" height="52"><use href="#houseland"/></svg>
  <div class="option" style="left:288px;top:172px"><span class="option-label">HOUSE<br>&amp;LAND</span></div>
  <div class="checkbox" style="left:368px;top:172px"></div>
</section>

<!-- Searches -->
<section class="card" style="left:392px;top:492px;width:416px;height:216px">
  <h2 class="card-title">I WOULD LIKE TO</h2>
  <svg class="icon" style="left:216px;top:22px" width="34" height="30" viewBox="0 0 34 30"><circle cx="12" cy="12" r="9" fill="none" stroke="#33a6d7" stroke-width="5"/><path d="M19 19 L30 27" stroke="#33a6d7" stroke-width="5" stroke-linecap="round"/></svg>
  <div class="option" style="left:12px;top:68px"><span class="option-label">ONLY WHAT I NEED <span class="help">?</span></span></div>
  <div class="option" style="left:12px;top:108px"><span class="option-label">STANDARD SEARCHES <span class="help">?</span></span></div>
  <div class="option" style="left:12px;top:148px"><span class="option-label">PREMIUM SEARCHES <span class="help">?</span></span></div>
  <div class="option" style="left:12px;top:186px"><span class="option-label">I DO NOT NEED SEARCHES <span class="help">?</span></span></div>
</section>

<aside class="tooltip">
  <div class="tooltip-body">
    <p class="tooltip-title">This Is A ToolTip Example</p>
    <ul class="tooltip-list">
      <li>Title Search x 2</li>
      <li>Council Rates Search</li>
      <li>Special Water Metre Read</li>
      <li>Land Tax Clearance Certificate</li>
    </ul>
  </div>
</aside>

<!-- Quote -->
<section class="card" style="left:178px;top:724px;width:414px;height:216px">
  <h2 class="card-title">I WANT MY QUOTE TO ?</h2>
  <svg class="icon" style="left:10px;top:92px" width="56" height="30" viewBox="0 0 56 30"><path d="M28 15 C20 3 4 3 4 15 C4 27 20 27 28 15 C36 3 52 3 52 15 C52 27 36 27 28 15 Z" fill="none" stroke="#33a6d7" stroke-width="3.5"/></svg>
  <div class="option" style="left:76px;top:92px"><span class="option-label">INCLUDE UNLIMITED<br>EXTENSIONS</span></div>
  <div class="checkbox" style="left:365px;top:92px"><svg width="48" height="40"><use href="#tick"/></svg></div>

  <svg class="icon" style="left:10px;top:164px" width="56" height="48" viewBox="0 0 56 48"><circle cx="36" cy="14" r="11" fill="none" stroke="#33a6d7" stroke-width="3"/><text x="36" y="20" font-family="Ubuntu,sans-serif" font-size="15" fill="#33a6d7" text-anchor="middle">$</text><rect x="2" y="30" width="10" height="16"/><path d="M12 32 L28 32 C34 32 34 38 28 38 L22 38 M24 38 L40 34 C46 32 48 38 44 40 L30 46 L12 46" fill="none" stroke="#33a6d7" stroke-width="3"/></svg>
  <div class="option" style="left:76px;top:164px"><span class="option-label">PAY FOR EXTENSIONS<br>IF I NEED THEM</span></div>
  <div class="checkbox" style="left:365px;top:164px"></div>
</section>

<!-- Contract -->
<section class="card" style="left:608px;top:724px;width:416px;height:216px">
  <h2 class="card-title">I HAVE ?</h2>
  <svg class="icon" style="left:10px;top:92px" width="48" height="52" viewBox="0 0 48 52"><path d="M4 2 L30 2 L38 10 L38 50 L4 50 Z" fill="none" stroke="#33a6d7" stroke-width="3.5"/><path d="M10 14 L28 14 M10 22 L30 22 M10 30 L24 30" stroke="#33a6d7" stroke-width="3"/><path d="M30 44 L44 22 L47 25 L33 46 Z"/><path d="M10 42 C14 36 16 46 22 40" fill="none" stroke="#33a6d7" stroke-width="2"/></svg>
  <div class="option" style="left:66px;top:92px"><span class="option-label">SIGNED A<br>CONTRACT</span></div>
  <div class="checkbox" style="left:364px;top:92px"></div>

  <svg class="icon" style="left:8px;top:166px" width="50" height="52" viewBox="0 0 50 52"><path d="M8 2 L34 2 L42 10 L42 50 L8 50 Z" fill="none" stroke="#33a6d7" stroke-width="3.5"/><circle cx="24" cy="28" r="19" fill="none" stroke="#222" stroke-width="5"/><path d="M11 15 L37 41" stroke="#222" stroke-width="5"/></svg>
  <div class="option" style="left:66px;top:164px"><span class="option-label">NOT SIGNED<br>A CONTRACT</span></div>
  <div class="checkbox" style="left:364px;top:164px"><svg width="48" height="40"><use href="#tick"/></svg></div>
</section>

<!-- Possibilities -->
<section class="card" style="left:392px;top:952px;width:416px;height:218px">
  <h2 class="card-title">ALLOW THE POSSIBILITY FOR ?</h2>
  <div class="option" style="left:14px;top:78px"><span class="option-label">TERMINATION OF QUOTE <span class="help">?</span></span></div>
  <div class="checkbox" style="left:364px;top:78px"></div>
  <div class="option" style="left:14px;top:130px"><span class="option-label">REASSION OF QUOTE <span class="help">?</span></span></div>
  <div class="checkbox" style="left:364px;top:130px"><svg width="48" height="40"><use href="#tick"/></svg></div>
  <div class="option" style="left:14px;top:181px"><span class="option-label">VARIATION OF QUOTE <span class="help">?</span></span></div>
  <div class="checkbox" style="left:364px;top:181px"></div>
</section>

</body>
</html>
```